Milos Meadow Plant Hire WEB

Milos Meadow are a small family owned business specialising in hire of indoor horticultural plants. They have been operating for more than 20 years in the local New Zealand market providing long and short term plant hire for businesses and events.

They offer a wide range of mostly tropical and indigenous plants for hire and Milos Meadow staff maintain all hire plants on a regular basis.

MORE PHOTOS AVAILABLE ON REQUEST if required

Please note - this should be a small 3 pager - home/about - products - gallery
Contact Us can be a button or on home page. Note - this is a small owner operated business.

Target Market(s)

Commercial, offices, entrance foyers, receptions, restaurants, promotions, trade shows, events, corporate and private functions

Industry/Entity Type

Business

Requirements
Must have
• Must remain integral to existing branding and include the current company logo. Should maintain existing corporate colours. Requires an enquiry page for people to contact the company via email (this can be a mailto page), also requires a page explaining about the company, and one detailing the types of hire available together with types of plans for hire. The site also needs a gallery that can be added to over time to show the various plants and their applications.
Nice to have
• It would be nice to have a facility on the gallery where a couple of detail lines could be added to explain the plant types, location etc

PREFER A WORDPRESS SOLUTION - BUT OPEN TO SUGGESTIONS
Should not have
• The site should not be overly complex. It should be simple for the client to self manage (add/ remove photos, edit text) It should be quick to load and simple to navigate.

```html
<!DOCTYPE html>
<html lang="en">
<head>
<meta charset="utf-8">
<title>Milos Meadow Plant Hire</title>
<link href="https://fonts.googleapis.com/css2?family=Open+Sans:wght@400;600&family=Roboto+Condensed:wght@300;400&family=Oswald:wght@300&family=Crimson+Text:wght@400;600&display=swap" rel="stylesheet">
<style>
:root{
  --green:#5f9a12;
  --green-light:#8cc63f;
  --green-dark:#2c4a0c;
  --green-deep:#1f3808;
  --label:#6f9a4a;
  --wine:#7a0d38;
  --text:#3d3d3d;
  --paper:#f4f5f0;
  --orange:#e8741c;
}
*{box-sizing:border-box;margin:0;padding:0}
html,body{width:1200px;height:2567px;overflow:hidden}
body{position:relative;background:var(--paper);font-family:"Open Sans",Arial,sans-serif;color:var(--text)}
.header{position:absolute;left:0;top:0;width:1200px;height:124px;background:linear-gradient(#86bf2e,#5c9412)}
.brand{position:absolute;left:145px;top:30px;font-family:"Crimson Text",Georgia,serif;font-size:50px;color:#fff}
.call{position:absolute;right:130px;top:20px;color:#fff;font-size:15px}
.call b{font-size:21px;font-weight:600}
.nav{position:absolute;right:127px;top:73px;display:flex;gap:28px}
.nav a{color:#fff;text-decoration:none;font-family:"Roboto Condensed",Arial,sans-serif;font-size:19px;letter-spacing:.5px}
.hero{position:absolute;left:0;top:124px;width:1200px;height:481px;background:linear-gradient(100deg,#c9b79e 0%,#e7e2d6 30%,#6f8a58 55%,#b9c6a4 75%,#dfe3d6 100%)}
.dots{position:absolute;left:998px;top:582px;display:flex;gap:5px}
.dots i{width:11px;height:11px;background:#fff;opacity:.8}
.dots i:first-child{opacity:1;background:#ddd}
.welcome{position:absolute;left:0;top:605px;width:1200px;height:400px;background:radial-gradient(ellipse at 50% 10%,#eef5dd,#e3efcc 70%)}
.welcome h1{position:absolute;left:156px;top:55px;font-family:"Roboto Condensed",Arial,sans-serif;font-weight:300;font-size:46px;color:#2a2a2a}
.welcome h1 span{color:var(--green)}
.welcome .copy{position:absolute;left:156px;top:128px;width:650px;font-size:14px;line-height:20px}
.welcome .copy p{margin-bottom:12px}
.grass{position:absolute;left:0;top:985px;width:1200px;height:52px;background:linear-gradient(#b7d97a,#4f8a14)}
.band{position:absolute;left:0;top:1037px;width:1200px;height:63px;background:linear-gradient(#3f7a0e,#5d9918);border-bottom-left-radius:50% 14px;border-bottom-right-radius:50% 14px}
.band h2{text-align:center;line-height:63px;font-family:"Oswald",Arial,sans-serif;font-weight:300;font-size:33px;letter-spacing:9px;color:#fff}
.panel{position:absolute;left:141px;width:918px;background:#fff;box-shadow:0 0 8px rgba(0,0,0,.18)}
.tile{position:absolute;overflow:hidden}
.tile .photo{position:absolute;inset:0}
.tile .label{position:absolute;left:0;right:0;bottom:0;height:34px;background:var(--label);color:#fff;text-align:center;line-height:34px;font-family:"Crimson Text",Georgia,serif;font-size:17px;letter-spacing:1px;text-transform:uppercase;white-space:nowrap}
.tile .label.big{height:78px;background:var(--wine);text-align:left;padding:11px 12px;line-height:27px;font-size:21px;letter-spacing:.3px}
.benefits-title{position:absolute;left:0;top:2030px;width:1200px;text-align:center;font-family:"Oswald",Arial,sans-serif;font-weight:300;font-size:32px;letter-spacing:8px;color:var(--green)}
.rule{position:absolute;top:2053px;height:1px;width:170px;background:#bbb}
.list{position:absolute;top:2118px;list-style:none;font-size:16px;line-height:37px}
.list li{position:relative;padding-left:26px}
.list li.two-line{line-height:29px;padding-top:4px;padding-bottom:4px}
.list li::before{content:"";position:absolute;left:0;top:13px;width:11px;height:11px;background:var(--orange);border-radius:0 60% 0 60%}
.footer{position:absolute;left:0;top:2419px;width:1200px;height:118px;background:var(--green-dark);color:#fff;font-size:13px}
.fnav{position:absolute;left:140px;top:20px}
.fline{position:absolute;left:138px;display:flex;align-items:center;gap:10px}
.social{position:absolute;right:138px;top:36px;display:flex;gap:10px}
.social i{width:40px;height:40px;border-radius:50%;background:#4d6b2c}
.copyright{position:absolute;left:0;top:2537px;width:1200px;height:30px;background:var(--green-deep);color:#ddd;text-align:center;line-height:30px;font-size:12px}
</style>
</head>
<body>
<header class="header">
  <div class="brand">Milos Meadow</div>
  <div class="call">Call Us: <b>0400 218 904</b></div>
  <nav class="nav"><a>HOME</a><a>ABOUT</a><a>PRODUCTS</a><a>GALLERY</a><a>CONTACT US</a></nav>
</header>
<div class="hero" role="img" aria-label="Living room with armchair and tall potted indoor plants by a window"></div>
<div class="dots"><i></i><i></i><i></i><i></i></div>

<section class="welcome">
  <h1>Welcome to <span>Milos Meadow</span></h1>
  <div class="copy">
    <p>Milos Meadow is a family owned, Christchurch based business established over 25 years ago.</p>
    <p>We can enhance your workplace by introducing quality indoor plants in attractive planters. Creating a natural green environment with Milos Meadow plants will help improve indoor air quality, increase staff wellness and productivity.</p>
    <p>Our range of tropical and native plants will enhance your conference or event by creating a more relaxing atmosphere for your delegates or clients. Milos Meadow staff can advise on plant arrangement, deliver and setup for each event.</p>
    <p>We are committed to providing prompt friendly service to all our customers ensuring that your workplace or function is enhanced with quality Milos Meadow plants.</p>
  </div>
</section>
<div class="grass" role="img" aria-label="Strip of green grass"></div>
<div class="band"><h2>PRODUCTS &amp; SERVICES</h2></div>

<section class="panel" style="top:1123px;height:411px">
  <div class="tile" style="left:15px;top:15px;width:291px;height:379px"><div class="photo" role="img" aria-label="Tall leafy plants in planters" style="background:linear-gradient(#e9efe2,#6f9a45)"></div><div class="label big">Long Term<br>Indoor Plant Hire</div></div>
  <div class="tile" style="left:315px;top:15px;width:290px;height:182px"><div class="photo" role="img" aria-label="Open plan office with plants" style="background:linear-gradient(#f1e4cf,#a9a08e)"></div><div class="label">Commercial Office Plant</div></div>
  <div class="tile" style="left:614px;top:15px;width:290px;height:182px"><div class="photo" role="img" aria-label="Reception desk with plants" style="background:linear-gradient(#4a3d35,#e9e3da)"></div><div class="label">Receptions Plant</div></div>
  <div class="tile" style="left:315px;top:210px;width:290px;height:184px"><div class="photo" role="img" aria-label="Staff in a showroom with plants" style="background:linear-gradient(#dfe5ea,#8a8a86)"></div><div class="label">Showrooms Plant</div></div>
  <div class="tile" style="left:614px;top:210px;width:290px;height:184px"><div class="photo" role="img" aria-label="Lounge seating around a planter" style="background:linear-gradient(#8a6e58,#5d6b45)"></div><div class="label">Hospitality Plant</div></div>
</section>

<section class="panel" style="top:1559px;height:409px">
  <div class="tile" style="left:15px;top:15px;width:291px;height:182px"><div class="photo" role="img" aria-label="Colourful shopfronts with potted plants" style="background:linear-gradient(90deg,#d9508e,#a8c07a)"></div><div class="label">Trade &amp; Events Plant</div></div>
  <div class="tile" style="left:315px;top:15px;width:290px;height:182px"><div class="photo" role="img" aria-label="Bright conference room with plant" style="background:linear-gradient(#c8dc6a,#f1f2ec)"></div><div class="label">Conferences Plant</div></div>
  <div class="tile" style="left:614px;top:15px;width:290px;height:376px"><div class="photo" role="img" aria-label="Conservatory filled with palms" style="background:linear-gradient(#5f6f58,#d6dccd)"></div><div class="label big">Short Term Indoor<br>&amp; Outdoor Plant Hire</div></div>
  <div class="tile" style="left:15px;top:208px;width:291px;height:183px"><div class="photo" role="img" aria-label="Promotional flower display" style="background:linear-gradient(#f0e9e0,#d9c44a)"></div><div class="label">Promotions Plant</div></div>
  <div class="tile" style="left:315px;top:208px;width:290px;height:183px"><div class="photo" role="img" aria-label="Wedding garden setting" style="background:linear-gradient(#c7558a,#6a8a4a)"></div><div class="label">Weddings Plant</div></div>
</section>

<div class="rule" style="left:330px"></div><div class="rule" style="left:700px"></div>
<h2 class="benefits-title">BENEFITS</h2>
<ul class="list" style="left:150px;width:420px">
  <li class="two-line">Family Owned Christchurch based businessesPromt<br>efficient and friendly</li>
  <li>7 day per week service</li>
  <li>On-site advice and quotes</li>
  <li>Competitive hire charges</li>
  <li>Quality plants and planters</li>
  <li>Regular plant maintenance</li>
</ul>
<ul class="list" style="left:616px;width:440px">
  <li>No fixed terms contract necessary</li>
  <li>Enhances the appearance of your workplace</li>
  <li>Provides a natural and tranquil environment</li>
  <li>Provides interior landscaping variety and versatility</li>
  <li>Provids a claming atmosphere for clients and staff</li>
  <li>No staff down time due to gardenin</li>
  <li>Speciment plants up to 2.5m tall available</li>
</ul>

<footer class="footer">
  <div class="fnav">Home &nbsp;|&nbsp; About &nbsp;|&nbsp; Products &nbsp;|&nbsp; Gallery &nbsp;|&nbsp; Contact Us</div>
  <div class="fline" style="top:48px">
    <svg width="14" height="18" viewBox="0 0 14 18"><path d="M7 0a7 7 0 0 0-7 7c0 5 7 11 7 11s7-6 7-11a7 7 0 0 0-7-7z" fill="#9cc36a"/><circle cx="7" cy="7" r="2.5" fill="#2c4a0c"/></svg>
    <span>18 Orchard Lane, Riverbend</span>
  </div>
  <div class="fline" style="top:80px">
    <svg width="16" height="16" viewBox="0 0 16 16"><path d="M3 1l3 3-2 2c1 2 3 4 6 6l2-2 3 3-2 2C7 15 1 9 1 3z" fill="#9cc36a"/></svg>
    <span>0400 218 904</span>
    <svg style="margin-left:30px" width="18" height="12" viewBox="0 0 18 12"><rect width="18" height="12" fill="#9cc36a"/><path d="M0 0l9 7 9-7" stroke="#2c4a0c" fill="none"/></svg>
    <span>info@milosmeadow.co.nz</span>
  </div>
  <div class="social"><i></i><i></i><i></i></div>
</footer>
<div class="copyright">Copyright© 2013 Milos Meadow. All Rights Reserved</div>
</body>
</html>
```